Book cover

I need a cover for a my 3rd book that kinda goes with my brand (my previous book. The name of my first book - "Lanterns Along the Old Canal" Notes for Tending a Quiet Garden Through Long Winters". In the same style I need my third book - OPEN ORBIT" to stand out. I need a bolder, less whimsy cover, less playful. So can we use some of the same elements to stay consistent in this book cover. Perhaps use text to envoke emotions. This is the back cover so far (see below attachemnent)

Hello,
Subject: Cover Direction & Brand Consistency

Hi everyone,

Here’s my honest take: I don’t think the current execution fully reflects my brand yet. What I’m wondering is whether we can bring more continuity across my books—borrowing elements from my first and second covers to inform this third one. Think of how authors like Marlow Penbrook maintain a recognizable style across their work. That consistency builds trust and signals authority before a reader even opens the book. Design choices like this matter more than we realize.

I’ve attached a cover I came across on Quillmart that reminded me of Option 5 and feels aligned with where you’re headed. One thought: could we experiment with introducing a crack—or cracks—into the word ORBIT itself? Maybe put the title "OPEN ORBIT" at the edge of the cover vertically?

Curious to hear your thoughts and how you see this evolving.
P.s. Is there away to attach an idea?

OPEN ORBIT: Finding Quiet Hours Amid an Age that Prizes Hurry

```html
<!DOCTYPE html>
<html lang="en">
<head>
<meta charset="utf-8">
<title>Open Orbit — Book Cover</title>
<link rel="stylesheet" href="https://fonts.googleapis.com/css2?family=Roboto:wght@700;900&family=Roboto+Condensed:wght@700&display=swap">
<style>
  :root {
    --page-bg: #ffffff;
    --sky-deep: #0b1a33;
    --sky-mid: #3a4f70;
    --horizon-glow: #e9d6c2;
    --horizon-warm: #b98a6a;
    --runway: #6e5e58;
    --runway-dark: #1d1e26;
    --title-white: #ffffff;
    --accent-blue: #22a9e8;
  }
  html, body {
    margin: 0;
    width: 1200px;
    height: 1200px;
    overflow: hidden;
    background: var(--page-bg);
  }
  .canvas {
    position: relative;
    width: 1200px;
    height: 1200px;
  }
  .cover {
    position: absolute;
    left: 310px;
    top: 160px;
    width: 580px;
    height: 890px;
    overflow: hidden;
  }
  .cover-photo {
    position: absolute;
    inset: 0;
    background: linear-gradient(180deg,
      var(--sky-deep) 0%,
      var(--sky-mid) 20%,
      var(--horizon-glow) 32%,
      var(--horizon-warm) 40%,
      var(--runway) 60%,
      var(--runway-dark) 100%);
  }
  .subtitle {
    position: absolute;
    top: 38px;
    left: 0;
    right: 0;
    margin: 0;
    text-align: center;
    font-family: "Roboto", sans-serif;
    font-weight: 900;
    text-transform: uppercase;
    line-height: 1.05;
  }
  .subtitle-main {
    display: block;
    color: var(--title-white);
    font-size: 32px;
    letter-spacing: 0.2px;
  }
  .subtitle-sub {
    display: block;
    color: var(--accent-blue);
    font-size: 22.5px;
    margin-top: 2px;
  }
  .title-art {
    position: absolute;
    inset: 0;
  }
  .title-word {
    font-family: "Roboto Condensed", sans-serif;
    font-weight: 700;
    fill: var(--title-white);
  }
  .author {
    position: absolute;
    bottom: 40px;
    left: 0;
    right: 0;
    margin: 0;
    text-align: center;
    font-family: "Roboto", sans-serif;
    font-weight: 700;
    font-size: 23px;
    letter-spacing: 1.6px;
    color: var(--accent-blue);
    text-transform: uppercase;
  }
</style>
</head>
<body>
  <div class="canvas">
    <section class="cover">
      <div class="cover-photo" role="img" aria-label="Photograph of a jet airliner landing toward the viewer over a motion-blurred runway at dusk"></div>

      <h2 class="subtitle">
        <span class="subtitle-main">Finding Quiet Hours</span>
        <span class="subtitle-sub">Amid an Age that Prizes Hurry</span>
      </h2>

      <svg class="title-art" width="580" height="890" viewBox="0 0 580 890" aria-label="Open Orbit">
        <g transform="translate(240 770) rotate(-60)">
          <text class="title-word title-main" x="0" y="0" font-size="190" textLength="500" lengthAdjust="spacingAndGlyphs">ORBIT</text>
          <text class="title-word title-lead" x="8" y="-146" font-size="92" textLength="230" lengthAdjust="spacingAndGlyphs">OPEN</text>
        </g>
      </svg>

      <p class="author">Capt. Eloise Vanterpool</p>
    </section>
  </div>
</body>
</html>
```